KOR Methodology infographic that shows flow of the process outlined on our web site

We are looking for a graphical representation of the methodology that is described on this web page: https://www.kor-example.com/about-kor/methodology/ We would like someone to be able to quickly understand our methodology and the key points outlined on the web page - the graphic should be able to do that.

Target Market(s)

Enterprise Companies with 1000+ employees

Industry/Entity Type

Information Technology

Font styles to use
Sans Serif

Colors
3277b5
abd036
faa54b

Requirements
Must have
• Must convey the method/process with enough detail to understand what the process is.
Nice to have
• Arrows or something showing flow would be great
Should not have
• Should not be "cartoony"

```html
<!DOCTYPE html>
<html lang="en">
<head>
<meta charset="utf-8">
<title>KOR Methodology</title>
<link href="https://fonts.googleapis.com/css2?family=Roboto:wght@400;500;700&display=swap" rel="stylesheet">
<style>
  :root {
    --bg: #f4f8ee;
    --blue: #3277b5;
    --orange: #faa54b;
    --red: #c23152;
    --green: #abd036;
    --navy: #1f2f5c;
    --line: #b9c0c4;
    --white: #ffffff;
  }
  html, body {
    margin: 0;
    width: 1200px;
    height: 1200px;
    overflow: hidden;
    background: var(--bg);
    font-family: "Roboto", Arial, sans-serif;
  }
  .infographic {
    position: absolute;
    left: 0;
    top: 266px;
    width: 1187px;
    height: 659px;
    transform: scale(1.011);
    transform-origin: 0 0;
  }
  .cycle { position: absolute; left: 0; top: 0; }
  .step-note {
    position: absolute;
    width: 278px;
    height: 116px;
    border-radius: 8px;
    box-sizing: border-box;
    padding: 0 10px;
    display: flex;
    align-items: center;
    justify-content: center;
    text-align: center;
    color: var(--white);
    font-size: 11.3px;
    line-height: 13.2px;
  }
  .step-note--consultation { left: 127px; top: 62px; background: var(--blue); }
  .step-note--assessment { left: 790px; top: 62px; background: var(--orange); }
  .step-note--implementation { left: 127px; top: 485px; background: var(--green); }
  .step-note--solution { left: 790px; top: 485px; background: var(--red); }
  .phase-label { font-family: "Roboto", Arial, sans-serif; font-weight: 500; font-size: 13px; fill: var(--white); }
  .phase-number { font-family: "Roboto", Arial, sans-serif; font-weight: 500; font-size: 21px; }
  .hub-name { font-family: "Roboto", Arial, sans-serif; font-weight: 700; font-size: 28px; fill: var(--navy); }
  .hub-title { font-family: "Roboto", Arial, sans-serif; font-weight: 700; font-size: 13px; fill: #1c1c1c; letter-spacing: 0.4px; }
</style>
</head>
<body>
<main class="infographic">
  <svg class="cycle" width="1187" height="659" viewBox="0 0 1187 659">
    <!-- connectors -->
    <g fill="none" stroke="var(--line)" stroke-width="1">
      <polyline points="405,120 439,120 471,177"/>
      <polyline points="790,120 756,120 722,180"/>
      <polyline points="405,545 441,545 473,486"/>
      <polyline points="790,545 755,545 722,486"/>
    </g>
    <g>
      <circle cx="405" cy="120" r="5" fill="var(--blue)"/>
      <circle cx="790" cy="120" r="5" fill="var(--orange)"/>
      <circle cx="405" cy="545" r="5" fill="var(--green)"/>
      <circle cx="790" cy="545" r="5" fill="var(--red)"/>
    </g>
    <!-- quadrants, centre 594,329 r 195 -->
    <path d="M592,327 L399,327 A195,195 0 0 1 592,134 Z" fill="var(--blue)"/>
    <path d="M596,327 L596,134 A195,195 0 0 1 789,327 Z" fill="var(--orange)"/>
    <path d="M596,331 L789,331 A195,195 0 0 1 596,524 Z" fill="var(--red)"/>
    <path d="M592,331 L592,524 A195,195 0 0 1 399,331 Z" fill="var(--green)"/>
    <!-- number notches -->
    <circle cx="419" cy="309" r="27" fill="var(--bg)"/>
    <circle cx="614" cy="151" r="27" fill="var(--bg)"/>
    <circle cx="768" cy="349" r="27" fill="var(--bg)"/>
    <circle cx="575" cy="502" r="27" fill="var(--bg)"/>
    <text class="phase-number" x="419" y="316" text-anchor="middle" fill="var(--blue)">01</text>
    <text class="phase-number" x="614" y="158" text-anchor="middle" fill="var(--orange)">02</text>
    <text class="phase-number" x="768" y="356" text-anchor="middle" fill="var(--red)">03</text>
    <text class="phase-number" x="575" y="509" text-anchor="middle" fill="var(--green)">04</text>
    <!-- hub -->
    <circle cx="594" cy="329" r="93" fill="none" stroke="var(--white)" stroke-width="7"/>
    <circle cx="594" cy="329" r="66" fill="var(--white)"/>
    <circle cx="552" cy="310" r="6" fill="var(--green)"/>
    <text class="hub-name" x="566" y="320">KOR</text>
    <text class="hub-title" x="594" y="353" text-anchor="middle">METHODOLOGY</text>
    <!-- phase labels -->
    <text class="phase-label" x="489" y="213" text-anchor="middle">INITIAL</text>
    <text class="phase-label" x="489" y="229" text-anchor="middle">CONSULTATION</text>
    <text class="phase-label" x="701" y="224" text-anchor="middle">ASSESSMENT</text>
    <text class="phase-label" x="702" y="415" text-anchor="middle">SOLUTION</text>
    <text class="phase-label" x="702" y="431" text-anchor="middle">DEVELOPMENT</text>
    <text class="phase-label" x="482" y="425" text-anchor="middle">IMPLEMENTATION</text>
  </svg>

  <p class="step-note step-note--consultation">A first conversation in any relationship is vitally important. This is especially true when beginning an IT project. Setting expectations and defining success are integral parts of the process. An initial consultation with KOR will be filled with questions and listening as we discover the concerns you have and consider the best approach to help you achieve your goals.</p>
  <p class="step-note step-note--assessment">Very often after an initial consultation is over, the process is best served by adding an assessment phase. This process can range from simple interviews to full enterprise evaluations. The assessment stage should end with the discovery of all pertinent information needed for the development of an effective solution.</p>
  <p class="step-note step-note--implementation">Upon acceptance of a quote and a subsequent purchase order, the certified KOR engineers proceed with your implementation.</p>
  <p class="step-note step-note--solution">Your KOR team includes members of the account management, engineering, and finance departments. After initial consultations and assessments are completed, your team convenes to design and draw up solutions for your consideration.</p>
</main>
</body>
</html>
```